Family business needs stationery redesign with new logo

Family owned company, established in 1987 wanting a brand 'refresh'. We are an electrical, refrigeration and construction company based in the Barkly Region Northern Territory, Australia. We have a new logo we would like to use which is uploaded along with our current letterhead and email signature. We are also dropping the word 'contractors' so please do not include this on any designs. Please note also, the 'orange' color used in our logo and designs should be Northern Territory red ochre which is as follows:

RGB (Hex): #C75B12
PantoneĀ® 159 C
CMYK: 1 / 74 / 100 / 7

We are needing our stationery redesigned using our new logo. Please include letterheads, business cards, envelopes, and email signatures.

We currently use our business letterheads for quotations, invoices, letters, HR matters, and internal memos.

We also need a separate simplified letterhead for internal paperwork such as employee leave forms, meeting agendas, and meeting minutes etc.
Updates

Reason: Needing more submissions of full package designs. We are wanting all our stationery, including business cards, letterheads, email signatures, envelopes, etc to be cohesive. We also require ALL the information, as supplied on our template letterhead, to be included on the new letterhead designs. including electrical license no.etc Thank you, K&M

Reason: needing more time as work has got in the way of looking over designs. A lot of designs not meeting the brief/criteria.

Industry/Entity Type

Business

Colors
0355a3
f37122

Requirements
Must have
• The 'orange' color used in the designs should be Northern Territory red ochre which is as follows:
• RGB (Hex): #C75B12
• PantoneĀ® 159 C
• CMYK: 1 / 74 / 100 / 7
• ***MUST INCLUDE ALL INFORMATION THAT IS ON OUR CURRENT LETTERHEAD***
Should not have
• Please do not include the word 'contractors'

```html
<!DOCTYPE html>
<html lang="en">
<head>
<meta charset="utf-8">
<title>K&amp;M email signature</title>
<link href="https://fonts.googleapis.com/css2?family=Open+Sans:wght@300;400;700&display=swap" rel="stylesheet">
<style>
  :root {
    --ochre: #C75B12;
    --navy: #24336D;
    --white: #ffffff;
    --muted: #b9bccb;
    --page: #f2f2f0;
  }
  html, body {
    margin: 0;
    padding: 0;
    width: 1200px;
    height: 806px;
    overflow: hidden;
    background: var(--page);
    font-family: "Open Sans", Arial, sans-serif;
  }
  .signature {
    position: absolute;
    left: 40px;
    top: 256px;
    width: 1120px;
    height: 294px;
    background: var(--navy);
    overflow: hidden;
  }
  .signature__band {
    position: absolute;
    inset: 0;
    width: 1120px;
    height: 294px;
  }
  .brand-name {
    position: absolute;
    left: 264px;
    top: 124px;
    transform: translate(-50%, -50%);
    margin: 0;
    font-size: 44px;
    font-weight: 400;
    line-height: 1;
    color: var(--white);
    white-space: nowrap;
  }
  .abn {
    position: absolute;
    left: 197px;
    top: 228px;
    margin: 0;
    font-size: 34px;
    font-weight: 300;
    line-height: 1;
    color: var(--white);
  }
  .person {
    position: absolute;
    left: 507px;
    top: 24px;
  }
  .person__name {
    margin: 0;
    font-size: 43px;
    font-weight: 400;
    line-height: 1;
    color: var(--white);
  }
  .person__role {
    margin: 12px 0 0 2px;
    font-size: 13.5px;
    font-weight: 700;
    line-height: 1;
    letter-spacing: 0.6px;
    color: var(--ochre);
    text-transform: uppercase;
  }
  .contact {
    position: absolute;
    left: 507px;
    top: 118px;
    margin: 0;
    padding: 0;
    list-style: none;
    font-size: 20px;
    line-height: 30px;
  }
  .contact__label { color: var(--ochre); }
  .contact__value { color: var(--muted); font-weight: 300; }
  .contact__value--strong { color: var(--white); font-weight: 400; }
</style>
</head>
<body>
  <section class="signature" aria-label="K&amp;M email signature">
    <svg class="signature__band" viewBox="0 0 1120 294" aria-hidden="true">
      <polygon points="0,0 361,0 173,294 0,294" fill="var(--ochre)"/>
    </svg>

    <p class="brand-name">K&amp;M</p>
    <p class="abn">ABN 62</p>

    <div class="person">
      <h1 class="person__name">LEIGH</h1>
      <p class="person__role">Corporate Services Manager</p>
    </div>

    <ul class="contact">
      <li><span class="contact__label">Address:</span> <span class="contact__value contact__value--strong">PO Box 4410, 52 Marlow St, Ridgeway NT 0870</span></li>
      <li><span class="contact__label">Ph:</span> <span class="contact__value">08 7741</span></li>
      <li><span class="contact__label">Cell:</span> <span class="contact__value">0455</span></li>
      <li><span class="contact__label">Email:</span> <span class="contact__value">@kmbuild.com.au</span></li>
      <li><span class="contact__label">Web:</span> <span class="contact__value">www.kmbuild.com.au</span></li>
    </ul>
  </section>
</body>
</html>
```